Simple psychologist website
Open brief, creative designs encouraged
Site map:
Home
our services
our psychologists
selective mutism
resources
contact

Current website:
http://mindsproutyouth.com.au/
Not in love with our logo, or colours etc - open brief
Happy for new font/style/logo for company name - if we choose a logo design from a designer who doesn't win the competition, we will award $50 for the logo and use it in the new website

Website made a few years ago for a sister company that we really like:
http://www.korrelpsychology.com.au/

Clean, credible and warm and friendly look & feel
stock photos OK, designer will be required to hand over any images used in the design as shown in the PSD

Target Market(s)

Adolescents with psychological issues and their families

Industry/Entity Type

Psychology

Number of Pages Required

2 page

Colors

Designer to choose colors to be used in the design.

Requirements
Must have
• One home page - simple with 2 or 3 small areas to tease and attract the user and one template page to suit all the other pages
• We like slides, we want to have 3 slides like korrelpsychology.com.au
• Three slide titles:
• 1. We specialise in many areas, find the right clinical psychologist for your family
• 2. Child Clinical Psychologists in Chatswood and Westmead
• 3. Resources
• Pages structurally similar to
• http://www.korrelpsychology.com.au/
• We like the 'featured' items, which in our case will have splash box titles (can be 3 or 4):
• 1. Selective Mutism
• 2. Is my child anxious?
• 3. Does my child have an eating disorder?
• 4. Parenting adolescents
• Does not need to be a copy of http://www.korrelpsychology.com.au/ and we are willing to accept outside-the-box thinking and design (we in fact encourage it)
• Owner of business wants to highlight Selective Mutism as they have specialists. Consider ways that may make this work.
• Design winner will be based on home page design but winning designer will be required to provide an additional but simpler 'standard' page template design based on the themes used in the winning design.

```html
<!DOCTYPE html>
<html lang="en">
<head>
<meta charset="utf-8">
<title>MindSprout – homepage slides</title>
<link href="https://fonts.googleapis.com/css2?family=Montserrat:wght@300;400;500;600&display=swap" rel="stylesheet">
<style>
:root{
  --stage:#6f80ee;
  --indigo:#33339a;
  --indigo-deep:#2a2c86;
  --ink:#3a3a4a;
  --muted:#7a7a8a;
  --icon:#4a4fd6;
  --pale:#eef1fd;
  --footer:#c3c9ef;
  --purple:#a46fe2;
  --white:#ffffff;
}
*{margin:0;padding:0;box-sizing:border-box}
html,body{width:1200px;height:967px;overflow:hidden;background:var(--stage);font-family:"Montserrat",sans-serif}
.page{position:absolute;top:18px;width:368px;height:922px;background:var(--white);overflow:hidden}
.page abs,.page .a{position:absolute}
.hero{position:absolute;left:0;top:0;width:368px;height:205px;background:var(--indigo)}
.hero-photo{position:absolute;inset:0}
.p1 .hero-photo{background:radial-gradient(ellipse at 72% 35%,#6a66c4 0%,#3f3fa6 35%,#2e2f8e 80%)}
.p2 .hero-photo{background:radial-gradient(ellipse at 55% 60%,#7a64b0 0%,#4c46a6 40%,#30318f 85%)}
.p3 .hero-photo{background:linear-gradient(120deg,#4648a8 0%,#5b5fbd 55%,#6d72c8 75%,#3e409f 100%)}
.brand{position:absolute;left:12px;top:12px;color:var(--white);font-weight:600;font-size:9px;display:flex;align-items:center;gap:4px}
.brand i{width:8px;height:8px;border:1px solid var(--white);border-radius:50%}
.brand-tag{position:absolute;left:12px;top:24px;color:#cfd2f5;font-size:3px}
.nav{position:absolute;left:128px;top:14px;display:flex;gap:12px;font-size:4.2px;color:#d8daf7}
.nav span:first-child{color:var(--white);font-weight:500}
.nav-line{position:absolute;left:0;right:0;top:29px;height:1px;background:rgba(255,255,255,.25)}
.nav-active{position:absolute;left:128px;top:28px;width:14px;height:2px;background:var(--white)}
.hero-text{position:absolute;left:66px;color:var(--white)}
.hero h1{font-weight:300;font-size:15.5px;line-height:20px}
.hero p{font-size:5px;line-height:8px;font-weight:400;margin-top:8px}
.hero .kicker{font-size:5px;margin-bottom:8px}
.rule{display:block;width:14px;height:1.5px;background:var(--white);margin-top:12px}
.btn-white{display:inline-block;margin-top:10px;width:72px;height:12px;border-radius:6px;background:var(--white);color:var(--indigo);font-size:4px;text-align:center;line-height:12px}
.dots{position:absolute;left:66px;top:186px;display:flex;gap:12px}
.dots b{width:6px;height:6px;border:1px solid var(--white);border-radius:50%}
.dots b.on{background:var(--white)}
.services{position:absolute;left:0;top:205px;width:368px;height:207px;text-align:center}
h2{font-weight:400;font-size:10px;color:var(--ink)}
.services h2{margin-top:24px}
.lead{font-size:3.8px;line-height:6.5px;color:var(--muted);width:124px;margin:10px auto 0}
.svc{position:absolute;width:110px;text-align:center;font-size:3.6px;line-height:6px;color:var(--muted)}
.svc .ic{width:24px;height:24px;border:1px solid #d7d9ee;border-radius:50%;margin:0 auto 4px;display:flex;align-items:center;justify-content:center}
.featured{position:absolute;left:0;top:412px;width:368px;height:213px;background:var(--indigo-deep)}
.feat-photo{position:absolute;left:0;top:0;width:230px;height:213px;background:radial-gradient(ellipse at 30% 30%,#6a4f9c 0%,#4a3f98 40%,rgba(42,44,134,0) 85%)}
.feat-main{position:absolute;left:66px;top:110px;width:110px;color:var(--white)}
.feat-main h3{font-weight:400;font-size:10.5px;line-height:13px}
.feat-main p{font-size:3.6px;line-height:6px;color:#a9abdc;margin-top:8px}
.btn-purple{display:block;margin-top:10px;width:72px;height:11px;border-radius:6px;background:var(--purple);color:var(--white);font-size:4px;line-height:11px;text-align:center}
.feat-item{position:absolute;left:197px;width:120px;color:var(--white)}
.feat-item h4{font-weight:400;font-size:6px;line-height:8px}
.feat-item p{font-size:3.6px;line-height:6px;color:#a9abdc;margin-top:3px}
.btn-line{display:block;margin-top:6px;width:51px;height:8px;border:1px solid var(--white);border-radius:4px;font-size:3.6px;line-height:6px;text-align:center}
.team{position:absolute;left:0;top:625px;width:368px;height:212px;background:var(--pale);text-align:center}
.team h2{margin-top:24px}
.team .lead{width:128px;margin-top:8px}
.member{position:absolute;top:65px;width:56px;text-align:left}
.member .ph{width:56px;height:81px;background:linear-gradient(180deg,#cfd1d6,#9ea1a8)}
.member .nm{font-size:5.2px;line-height:8px;color:var(--ink);margin-top:5px}
.member .rl{font-size:3px;color:var(--muted);margin-top:3px}
.member .ln{width:14px;height:1.5px;background:var(--ink);margin-top:6px}
.foot{position:absolute;left:0;top:837px;width:368px;height:85px;background:var(--footer)}
.col{position:absolute;top:26px;width:64px;font-size:3.4px;line-height:5.5px;color:#3b3f7a}
.col b{font-weight:600;display:block;margin-bottom:3px}
</style>
</head>
<body>

<!-- Slide 1 -->
<section class="page p1" style="left:24px">
  <div class="hero">
    <div class="hero-photo" role="img" aria-label="Young man leaning against a tree in a forest, blue tint"></div>
    <div class="brand"><i></i>MindSprout</div>
    <div class="brand-tag">Child, Adolescent &amp; Family Psychology</div>
    <nav class="nav"><span>Home</span><span>About Us</span><span>For Parents</span><span>For Professionals</span><span>For Teens</span><span>Blog</span><span>Contact</span></nav>
    <div class="nav-line"></div><div class="nav-active"></div>
    <div class="hero-text" style="top:40px">
      <h1>We specialise<br>in many areas</h1>
      <p>find the right clinical psychologist<br>for your family</p>
      <span class="rule"></span>
    </div>
    <div class="dots"><b class="on"></b><b></b><b></b></div>
  </div>
  <div class="services">
    <h2>Our Services</h2>
    <p class="lead">We are a group of clinical psychologists at Chatswood and Westmead (Sydney). We provide a range of services including the following</p>
    <div class="svc" style="left:40px;top:76px"><div class="ic"><svg width="12" height="12" viewBox="0 0 12 12"><path d="M6 10.5 1.5 6A2.6 2.6 0 0 1 6 2.6 2.6 2.6 0 0 1 10.5 6Z" fill="none" stroke="#4a4fd6" stroke-width="1.2"/></svg></div>individual counselling and therapy for kids, teens and families</div>
    <div class="svc" style="left:193px;top:76px"><div class="ic"><svg width="12" height="12" viewBox="0 0 12 12" fill="#4a4fd6"><circle cx="2.5" cy="3" r="1.2"/><circle cx="6" cy="2.5" r="1.3"/><circle cx="9.5" cy="3" r="1.2"/><rect x="1.5" y="5" width="2" height="5"/><rect x="5" y="4.5" width="2" height="5.5"/><rect x="8.5" y="5" width="2" height="5"/></svg></div>family consultations</div>
    <div class="svc" style="left:40px;top:129px"><div class="ic"><svg width="12" height="12" viewBox="0 0 12 12"><rect x="5" y="1.5" width="6" height="5" fill="none" stroke="#4a4fd6"/><circle cx="2.5" cy="4" r="1.2" fill="#4a4fd6"/><rect x="1.5" y="6" width="2" height="5" fill="#4a4fd6"/></svg></div>seminars and training with schools</div>
    <div class="svc" style="left:193px;top:129px"><div class="ic"><svg width="12" height="12" viewBox="0 0 12 12" fill="#4a4fd6"><circle cx="6" cy="3" r="1.6"/><path d="M2 11 4 5.5h4L10 11Z"/></svg></div>Brief group programmes for anxiety, stress and body image concerns for adolescents</div>
  </div>
  <div class="featured">
    <div class="feat-photo" role="img" aria-label="Child sitting quietly outdoors, purple tint"></div>
    <div class="feat-main"><h3>Selective Mutism In Children</h3><p>Elena Varga, Clinical Psychologist at MindSprout has many years of working with children with selective mutism. She is currently also</p><span class="btn-purple">Read More</span></div>
    <div class="feat-item" style="top:28px"><h4>Why Is My Child Anxious?</h4><p>Lorem ipsum dolor sit amet, consectetur adipiscing elit, sed do eiusmod tempor et dolore magna aliqua</p><span class="btn-line">Read More</span></div>
    <div class="feat-item" style="top:84px"><h4>Does My Child Have An<br>Eating Disorder?</h4><p>Lorem ipsum dolor sit amet, consectetur adipiscing elit, sed do eiusmod tempor et dolore magna aliqua</p><span class="btn-line">Read More</span></div>
    <div class="feat-item" style="top:150px"><h4>Parenting Adolescents</h4><p>Lorem ipsum dolor sit amet, consectetur adipiscing elit, sed do eiusmod tempor et dolore magna aliqua</p><span class="btn-line">Read More</span></div>
  </div>
  <div class="team">
    <h2>Meet Our Psychologists</h2>
    <p class="lead">Lorem ipsum dolor sit amet, consectetur adipiscing elit, sed do eiusmod tempor incididunt ut labore et dolore magna aliqua.</p>
    <div class="member" style="left:54px"><div class="ph" role="img" aria-label="Portrait of psychologist"></div><div class="nm">Daniel<br>Hartley</div><div class="rl">Specialist in child Psychology</div><div class="ln"></div></div>
    <div class="member" style="left:122px"><div class="ph" role="img" aria-label="Portrait of psychologist"></div><div class="nm">Daniel<br>Hartley</div><div class="rl">Specialist in child Psychology</div><div class="ln"></div></div>
    <div class="member" style="left:190px"><div class="ph" role="img" aria-label="Portrait of psychologist"></div><div class="nm">Daniel<br>Hartley</div><div class="rl">Specialist in child Psychology</div><div class="ln"></div></div>
    <div class="member" style="left:258px"><div class="ph" role="img" aria-label="Portrait of psychologist"></div><div class="nm">Daniel<br>Hartley</div><div class="rl">Specialist in child Psychology</div><div class="ln"></div></div>
  </div>
  <footer class="foot">
    <div class="col" style="left:58px"><b>Phone: 0400 218 905</b>Fax: (02) 9000 4417<br><br>Email: hello@<br>mindsproutyouth.com.au</div>
    <div class="col" style="left:122px"><b>Westmead</b>Suite 12, level 2<br>Parkside Health Rooms<br>40 Linden Road<br>Westmead NSW 2145</div>
    <div class="col" style="left:190px"><b>Chatswood</b>Suite 4<br>18 Oakleigh Lane<br>Chatswood NSW 2067</div>
    <div class="col" style="left:258px"><b>Postal Address</b>MindSprout<br>PO Box 742<br>Westmead NSW 2145</div>
  </footer>
</section>

<!-- Slide 2 -->
<section class="page p2" style="left:416px">
  <div class="hero">
    <div class="hero-photo" role="img" aria-label="Young woman on an autumn park path, blue tint"></div>
    <div class="brand"><i></i>MindSprout</div>
    <div class="brand-tag">Child, Adolescent &amp; Family Psychology</div>
    <nav class="nav"><span>Home</span><span>About Us</span><span>For Parents</span><span>For Professionals</span><span>For Teens</span><span>Blog</span><span>Contact</span></nav>
    <div class="nav-line"></div><div class="nav-active"></div>
    <div class="hero-text" style="top:42px">
      <div class="kicker">Child Clinical Psychologists in</div>
      <h1>Chatswood<br>and Westmead</h1>
      <span class="rule"></span>
    </div>
    <div class="dots"><b></b><b class="on"></b><b></b></div>
  </div>
  <div class="services">
    <h2>Our Services</h2>
    <p class="lead">We are a group of clinical psychologists at Chatswood and Westmead (Sydney). We provide a range of services including the following</p>
    <div class="svc" style="left:40px;top:76px"><div class="ic"><svg width="12" height="12" viewBox="0 0 12 12"><path d="M6 10.5 1.5 6A2.6 2.6 0 0 1 6 2.6 2.6 2.6 0 0 1 10.5 6Z" fill="none" stroke="#4a4fd6" stroke-width="1.2"/></svg></div>individual counselling and therapy for kids, teens and families</div>
    <div class="svc" style="left:193px;top:76px"><div class="ic"><svg width="12" height="12" viewBox="0 0 12 12" fill="#4a4fd6"><circle cx="2.5" cy="3" r="1.2"/><circle cx="6" cy="2.5" r="1.3"/><circle cx="9.5" cy="3" r="1.2"/><rect x="1.5" y="5" width="2" height="5"/><rect x="5" y="4.5" width="2" height="5.5"/><rect x="8.5" y="5" width="2" height="5"/></svg></div>family consultations</div>
    <div class="svc" style="left:40px;top:129px"><div class="ic"><svg width="12" height="12" viewBox="0 0 12 12"><rect x="5" y="1.5" width="6" height="5" fill="none" stroke="#4a4fd6"/><circle cx="2.5" cy="4" r="1.2" fill="#4a4fd6"/><rect x="1.5" y="6" width="2" height="5" fill="#4a4fd6"/></svg></div>seminars and training with schools</div>
    <div class="svc" style="left:193px;top:129px"><div class="ic"><svg width="12" height="12" viewBox="0 0 12 12" fill="#4a4fd6"><circle cx="6" cy="3" r="1.6"/><path d="M2 11 4 5.5h4L10 11Z"/></svg></div>Brief group programmes for anxiety, stress and body image concerns for adolescents</div>
  </div>
  <div class="featured">
    <div class="feat-photo" role="img" aria-label="Child sitting quietly outdoors, purple tint"></div>
    <div class="feat-main"><h3>Selective Mutism In Children</h3><p>Elena Varga, Clinical Psychologist at MindSprout has many years of working with children with selective mutism. She is currently also</p><span class="btn-purple">Read More</span></div>
    <div class="feat-item" style="top:28px"><h4>Why Is My Child Anxious?</h4><p>Lorem ipsum dolor sit amet, consectetur adipiscing elit, sed do eiusmod tempor et dolore magna aliqua</p><span class="btn-line">Read More</span></div>
    <div class="feat-item" style="top:84px"><h4>Does My Child Have An<br>Eating Disorder?</h4><p>Lorem ipsum dolor sit amet, consectetur adipiscing elit, sed do eiusmod tempor et dolore magna aliqua</p><span class="btn-line">Read More</span></div>
    <div class="feat-item" style="top:150px"><h4>Parenting Adolescents</h4><p>Lorem ipsum dolor sit amet, consectetur adipiscing elit, sed do eiusmod tempor et dolore magna aliqua</p><span class="btn-line">Read More</span></div>
  </div>
  <div class="team">
    <h2>Meet Our Psychologists</h2>
    <p class="lead">Lorem ipsum dolor sit amet, consectetur adipiscing elit, sed do eiusmod tempor incididunt ut labore et dolore magna aliqua.</p>
    <div class="member" style="left:54px"><div class="ph" role="img" aria-label="Portrait of psychologist"></div><div class="nm">Daniel<br>Hartley</div><div class="rl">Specialist in child Psychology</div><div class="ln"></div></div>
    <div class="member" style="left:122px"><div class="ph" role="img" aria-label="Portrait of psychologist"></div><div class="nm">Daniel<br>Hartley</div><div class="rl">Specialist in child Psychology</div><div class="ln"></div></div>
    <div class="member" style="left:190px"><div class="ph" role="img" aria-label="Portrait of psychologist"></div><div class="nm">Daniel<br>Hartley</div><div class="rl">Specialist in child Psychology</div><div class="ln"></div></div>
    <div class="member" style="left:258px"><div class="ph" role="img" aria-label="Portrait of psychologist"></div><div class="nm">Daniel<br>Hartley</div><div class="rl">Specialist in child Psychology</div><div class="ln"></div></div>
  </div>
  <footer class="foot">
    <div class="col" style="left:58px"><b>Phone: 0400 218 905</b>Fax: (02) 9000 4417<br><br>Email: hello@<br>mindsproutyouth.com.au</div>
    <div class="col" style="left:122px"><b>Westmead</b>Suite 12, level 2<br>Parkside Health Rooms<br>40 Linden Road<br>Westmead NSW 2145</div>
    <div class="col" style="left:190px"><b>Chatswood</b>Suite 4<br>18 Oakleigh Lane<br>Chatswood NSW 2067</div>
    <div class="col" style="left:258px"><b>Postal Address</b>MindSprout<br>PO Box 742<br>Westmead NSW 2145</div>
  </footer>
</section>

<!-- Slide 3 -->
<section class="page p3" style="left:809px">
  <div class="hero">
    <div class="hero-photo" role="img" aria-label="Hands holding an open printed booklet on a desk, blue tint"></div>
    <div class="brand"><i></i>MindSprout</div>
    <div class="brand-tag">Child, Adolescent &amp; Family Psychology</div>
    <nav class="nav"><span>Home</span><span>About Us</span><span>For Parents</span><span>For Professionals</span><span>For Teens</span><span>Blog</span><span>Contact</span></nav>
    <div class="nav-line"></div><div class="nav-active"></div>
    <div class="hero-text" style="top:40px">
      <h1>Extra<br>Resources</h1>
      <p>View some of the brilliant resources we<br>have by clicking the button below</p>
      <span class="btn-white">Read More</span>
    </div>
    <div class="dots"><b></b><b></b><b class="on"></b></div>
  </div>
  <div class="services">
    <h2>Our Services</h2>
    <p class="lead">We are a group of clinical psychologists at Chatswood and Westmead (Sydney). We provide a range of services including the following</p>
    <div class="svc" style="left:40px;top:76px"><div class="ic"><svg width="12" height="12" viewBox="0 0 12 12"><path d="M6 10.5 1.5 6A2.6 2.6 0 0 1 6 2.6 2.6 2.6 0 0 1 10.5 6Z" fill="none" stroke="#4a4fd6" stroke-width="1.2"/></svg></div>individual counselling and therapy for kids, teens and families</div>
    <div class="svc" style="left:193px;top:76px"><div class="ic"><svg width="12" height="12" viewBox="0 0 12 12" fill="#4a4fd6"><circle cx="2.5" cy="3" r="1.2"/><circle cx="6" cy="2.5" r="1.3"/><circle cx="9.5" cy="3" r="1.2"/><rect x="1.5" y="5" width="2" height="5"/><rect x="5" y="4.5" width="2" height="5.5"/><rect x="8.5" y="5" width="2" height="5"/></svg></div>family consultations</div>
    <div class="svc" style="left:40px;top:129px"><div class="ic"><svg width="12" height="12" viewBox="0 0 12 12"><rect x="5" y="1.5" width="6" height="5" fill="none" stroke="#4a4fd6"/><circle cx="2.5" cy="4" r="1.2" fill="#4a4fd6"/><rect x="1.5" y="6" width="2" height="5" fill="#4a4fd6"/></svg></div>seminars and training with schools</div>
    <div class="svc" style="left:193px;top:129px"><div class="ic"><svg width="12" height="12" viewBox="0 0 12 12" fill="#4a4fd6"><circle cx="6" cy="3" r="1.6"/><path d="M2 11 4 5.5h4L10 11Z"/></svg></div>Brief group programmes for anxiety, stress and body image concerns for adolescents</div>
  </div>
  <div class="featured">
    <div class="feat-photo" role="img" aria-label="Child sitting quietly outdoors, purple tint"></div>
    <div class="feat-main"><h3>Selective Mutism In Children</h3><p>Elena Varga, Clinical Psychologist at MindSprout has many years of working with children with selective mutism. She is currently also</p><span class="btn-purple">Read More</span></div>
    <div class="feat-item" style="top:28px"><h4>Why Is My Child Anxious?</h4><p>Lorem ipsum dolor sit amet, consectetur adipiscing elit, sed do eiusmod tempor et dolore magna aliqua</p><span class="btn-line">Read More</span></div>
    <div class="feat-item" style="top:84px"><h4>Does My Child Have An<br>Eating Disorder?</h4><p>Lorem ipsum dolor sit amet, consectetur adipiscing elit, sed do eiusmod tempor et dolore magna aliqua</p><span class="btn-line">Read More</span></div>
    <div class="feat-item" style="top:150px"><h4>Parenting Adolescents</h4><p>Lorem ipsum dolor sit amet, consectetur adipiscing elit, sed do eiusmod tempor et dolore magna aliqua</p><span class="btn-line">Read More</span></div>
  </div>
  <div class="team">
    <h2>Meet Our Psychologists</h2>
    <p class="lead">Lorem ipsum dolor sit amet, consectetur adipiscing elit, sed do eiusmod tempor incididunt ut labore et dolore magna aliqua.</p>
    <div class="member" style="left:54px"><div class="ph" role="img" aria-label="Portrait of psychologist"></div><div class="nm">Daniel<br>Hartley</div><div class="rl">Specialist in child Psychology</div><div class="ln"></div></div>
    <div class="member" style="left:122px"><div class="ph" role="img" aria-label="Portrait of psychologist"></div><div class="nm">Daniel<br>Hartley</div><div class="rl">Specialist in child Psychology</div><div class="ln"></div></div>
    <div class="member" style="left:190px"><div class="ph" role="img" aria-label="Portrait of psychologist"></div><div class="nm">Daniel<br>Hartley</div><div class="rl">Specialist in child Psychology</div><div class="ln"></div></div>
    <div class="member" style="left:258px"><div class="ph" role="img" aria-label="Portrait of psychologist"></div><div class="nm">Daniel<br>Hartley</div><div class="rl">Specialist in child Psychology</div><div class="ln"></div></div>
  </div>
  <footer class="foot">
    <div class="col" style="left:58px"><b>Phone: 0400 218 905</b>Fax: (02) 9000 4417<br><br>Email: hello@<br>mindsproutyouth.com.au</div>
    <div class="col" style="left:122px"><b>Westmead</b>Suite 12, level 2<br>Parkside Health Rooms<br>40 Linden Road<br>Westmead NSW 2145</div>
    <div class="col" style="left:190px"><b>Chatswood</b>Suite 4<br>18 Oakleigh Lane<br>Chatswood NSW 2067</div>
    <div class="col" style="left:258px"><b>Postal Address</b>MindSprout<br>PO Box 742<br>Westmead NSW 2145</div>
  </footer>
</section>

</body>
</html>
```